Business Cards for Internet Security Company

Awesome designers! This is the opportunity to help design cards for a forward thinking network security company. They use threat information gathered from peer groups to make intelligent decisions on what threats are relevant and which arent. ( not that you need this to do designs, but just so you know where they are coming from. ) :-)

We'd like to see a two side design and the deliverables will be in illustrator 4. The logo is attached and the logo colors are attached in the JPG and I've attached a an eps of the logo and icon

Security

```html
<!DOCTYPE html>
<html lang="en">
<head>
<meta charset="utf-8">
<title>Kelvane Business Cards</title>
<link href="https://fonts.googleapis.com/css2?family=Questrial&family=Roboto:wght@400;700&display=swap" rel="stylesheet">
<style>
  :root {
    --page: #ecebe8;
    --card: #ffffff;
    --brand: #2f5f86;
    --navy-deep: #0f2d4a;
    --navy-mid: #2b5677;
    --steel: #6a97b4;
    --stripe: #5b86c4;
    --ink-light: #ffffff;
    --icon: #cfe0ee;
  }
  * { box-sizing: border-box; margin: 0; padding: 0; }
  html, body { width: 1200px; height: 913px; overflow: hidden; }
  body {
    background: var(--page);
    font-family: "Questrial", sans-serif;
    position: relative;
  }
  .card {
    position: absolute;
    top: 302px;
    width: 540px;
    height: 309px;
    background: var(--card);
    box-shadow: 0 2px 10px rgba(0,0,0,0.15);
    overflow: hidden;
  }
  .card--front { left: 40px; }
  .card--back { left: 620px; }

  .wordmark {
    font-family: "Questrial", sans-serif;
    color: var(--brand);
    font-weight: 400;
    letter-spacing: 1px;
    position: absolute;
    white-space: nowrap;
  }
  .card--front .wordmark {
    font-size: 92px;
    left: 80px;
    top: 100px;
    display: flex;
    align-items: center;
    gap: 18px;
  }
  .brand-dot {
    width: 54px; height: 54px;
    border-radius: 50%;
    background: var(--brand);
    display: inline-block;
  }
  .card--back .wordmark {
    font-size: 48px;
    left: 34px;
    top: 100px;
  }

  .back-panel { position: absolute; inset: 0; }

  .holder {
    position: absolute;
    left: 30px;
    bottom: 12px;
    color: var(--ink-light);
    font-family: "Roboto", sans-serif;
  }
  .holder__name { font-size: 16px; font-weight: 700; line-height: 20px; }
  .holder__title { font-size: 13px; line-height: 18px; padding-left: 14px; }

  .contact {
    position: absolute;
    right: 16px;
    top: 56px;
    list-style: none;
    font-family: "Roboto", sans-serif;
    color: var(--ink-light);
    font-size: 12px;
    line-height: 20px;
  }
  .contact li { display: flex; justify-content: flex-end; align-items: center; gap: 8px; }
  .contact svg { width: 12px; height: 12px; flex: none; }
  .contact .no-icon { padding-right: 20px; }
</style>
</head>
<body>

<section class="card card--front" aria-label="Card front">
  <div class="wordmark"><span class="brand-dot"></span>Kelvane</div>
</section>

<section class="card card--back" aria-label="Card back">
  <svg class="back-panel" viewBox="0 0 540 309" width="540" height="309" aria-hidden="true">
    <defs>
      <linearGradient id="panelFill" x1="0" y1="1" x2="1" y2="0">
        <stop offset="0" stop-color="#0f2d4a"/>
        <stop offset="0.55" stop-color="#2b5677"/>
        <stop offset="1" stop-color="#6a97b4"/>
      </linearGradient>
    </defs>
    <path d="M330 0 C330 170 220 228 0 242 L0 309 L540 309 L540 0 Z" fill="url(#panelFill)"/>
    <path d="M316 0 C316 165 210 220 0 234" fill="none" stroke="#5b86c4" stroke-width="5"/>
  </svg>

  <div class="wordmark">Kelvane</div>

  <ul class="contact">
    <li>Your Address
      <svg viewBox="0 0 12 12"><path d="M6 0.5a4 4 0 0 1 4 4c0 3-4 7-4 7s-4-4-4-7a4 4 0 0 1 4-4z" fill="#cfe0ee"/><circle cx="6" cy="4.5" r="1.5" fill="#2b5677"/></svg>
    </li>
    <li class="no-icon">in just two line</li>
    <li>(000) 000.000.000
      <svg viewBox="0 0 12 12"><rect x="1" y="4" width="10" height="7" rx="1.5" fill="#cfe0ee"/><path d="M2 4 Q6 0 10 4" fill="none" stroke="#cfe0ee" stroke-width="1.6"/></svg>
    </li>
    <li>yourname@yourwebsite.com
      <svg viewBox="0 0 12 12"><rect x="0.5" y="2" width="11" height="8" fill="#cfe0ee"/><path d="M0.5 2 L6 7 L11.5 2" fill="none" stroke="#2b5677" stroke-width="1"/></svg>
    </li>
    <li>www.yourwebsite.com
      <svg viewBox="0 0 12 12"><circle cx="6" cy="6" r="5.3" fill="#cfe0ee"/><path d="M0.7 6 H11.3 M6 0.7 C3 3 3 9 6 11.3 M6 0.7 C9 3 9 9 6 11.3" fill="none" stroke="#2b5677" stroke-width="0.8"/></svg>
    </li>
  </ul>

  <div class="holder">
    <p class="holder__name">Your Name</p>
    <p class="holder__title">Title</p>
  </div>
</section>

</body>
</html>
```